Create a Graphic About YOURSELF and PixelHarbor

PixelHarbor would like you (designers) to create an awesome graphic to promote YOURSELF and your profile on PixelHarbor!

Your graphic should communicate your name, your services and should mention PixelHarbor.

The design should be perfect for sharing on Chatterly. Here's an example of what we'd like http://blog.pixelharbor-example.ca/article/333/pixelharbor-launches-3000-hire-me-social-design-contest

Once you submitted your design, we'd love you to share the design ('advertisement') and promote yourself and PixelHarbor to your friends and potential customers. So make your submissions great and get your friends to vote for your design by 'Liking' it on Chatterly!

Prizes:
$1500 - "PixelHarbor Community" prize awarded to the designer with the most Chatterly 'Likes'
5 x $50 for the next 5 'most liked' designs on Chatterly

$1000 - "Hire Me" prize awarded to the designer who receives the most client invites
5 x $50 for the next 5 'most invited' designers

In summary, this is a great opportunity for you to increase your exposure to PixelHarbor customers and win cash prizes. Show off your design skills and get hired by PixelHarbor customers from around the world!

Target Market(s)

Fans, friends and customers of YOU

Industry/Entity Type

Cash

Requirements
Must have
• 1) Include your PixelHarbor user name on the graphic so customers can find you in the PixelHarbor Designer Directory
2) Include the tagline "Hire Me on PixelHarbor.com!" in your graphic design.
3) Share your design's URL on our Chatterly wall at http://chatterly-example.com/pixelharbor and get your friends to 'like' your design.
Nice to have
• 1) Include a tagline that expresses your design approach/philosophy
2) Artwork dimensions: 403 x 403 px
3) You can submit more than 1 design!
Should not have
• You must own the copyright of any images you use including stock imagery.

```html
<!DOCTYPE html>
<html lang="en">
<head>
<meta charset="utf-8">
<title>Fluxline Studio – Hire Me on PixelHarbor</title>
<link rel="stylesheet" href="https://fonts.googleapis.com/css2?family=Exo+2:wght@300&display=swap">
<style>
  :root {
    --brand-pink: #ec1e79;
    --ink-grey: #58595b;
    --paper-white: #ffffff;
    --texture-light: #f4f4f4;
    --texture-mid: #d2d2d2;
    --texture-vein: #e7b9c9;
    --type: "Exo 2", sans-serif;
  }
  html, body {
    margin: 0;
    padding: 0;
    overflow: hidden;
    background: var(--paper-white);
  }
  .cover {
    position: relative;
    width: 1200px;
    height: 494px;
    overflow: hidden;
    font-family: var(--type);
    font-weight: 300;
    background: var(--brand-pink);
  }
  .texture-field {
    position: absolute;
    left: 0;
    top: 55px;
    width: 1200px;
    height: 338px;
    background:
      radial-gradient(ellipse 45% 60% at 62% 50%, var(--texture-light) 0%, rgba(244,244,244,0) 100%),
      linear-gradient(135deg, var(--texture-vein) 0%, var(--texture-mid) 30%, var(--texture-light) 55%, var(--texture-mid) 80%, var(--texture-vein) 100%);
  }
  .band-left {
    position: absolute;
    left: 0;
    top: 113px;
    width: 651px;
    height: 191px;
    background: var(--brand-pink);
  }
  .band-right {
    position: absolute;
    left: 1150px;
    top: 113px;
    width: 50px;
    height: 191px;
    background: var(--brand-pink);
  }
  .platform-tag {
    position: absolute;
    left: 192px;
    top: 89px;
    width: 150px;
    height: 34px;
    background: var(--paper-white);
    transform: rotate(-17deg);
    display: flex;
    align-items: center;
    justify-content: center;
    gap: 6px;
    box-shadow: 0 1px 3px rgba(0,0,0,0.25);
  }
  .platform-tag__dot {
    width: 12px;
    height: 12px;
    border-radius: 50%;
    background: var(--ink-grey);
  }
  .platform-tag__name {
    font-size: 19px;
    color: var(--ink-grey);
    line-height: 1;
  }
  .values {
    position: absolute;
    right: 555px;
    top: 116px;
    margin: 0;
    padding: 0;
    list-style: none;
    text-align: right;
    color: var(--paper-white);
    font-size: 32px;
    line-height: 47px;
    letter-spacing: 0.5px;
  }
  .studio-name {
    position: absolute;
    left: 660px;
    top: 118px;
    width: 485px;
    margin: 0;
    color: var(--ink-grey);
    font-weight: 300;
    text-align: center;
    line-height: 0.95;
  }
  .studio-name__main {
    display: block;
    font-size: 104px;
    letter-spacing: -2px;
  }
  .studio-name__sub {
    display: block;
    font-size: 70px;
    letter-spacing: 2px;
  }
  .tagline {
    position: absolute;
    right: 13px;
    top: 428px;
    margin: 0;
    color: var(--paper-white);
    font-size: 15px;
    letter-spacing: 0.2px;
  }
</style>
</head>
<body>
  <main class="cover">
    <div class="texture-field" role="img" aria-label="Soft grey marbled background with faint pink cracked veins"></div>
    <div class="band-left"></div>
    <div class="band-right"></div>

    <div class="platform-tag">
      <span class="platform-tag__dot"></span>
      <span class="platform-tag__name">PixelHarbor</span>
    </div>

    <ul class="values">
      <li>Creative</li>
      <li>Unique</li>
      <li>Timless</li>
      <li>Functional</li>
    </ul>

    <h1 class="studio-name">
      <span class="studio-name__main">Fluxline</span>
      <span class="studio-name__sub">Studio</span>
    </h1>

    <p class="tagline">We create bodes for your IDEAS to Born in, live within and meet the world</p>
  </main>
</body>
</html>
```